Personal Hygiene company needs packaging design

Hello everyone!
We need packaging designed for our new product - a cloth diaper sprayer. It is a personal hygiene tool used to clean cotton reusable diapers, but also doubles up as a personal hygiene tool (bidet). Please see following links of sellers of similar products:
http://www.shopvendra.example/gp/product/K027Q418T3
http://www.shopvendra.example/gp/product/K03LWMA8ZD
I have attached the following:
- Company logo
- 3D modeled images of the products that form part of the set within the package
- Image of instructions which should be on the back of the box
- word document with the relevant information that should appear on the packaging.
The dimensions of the packaging should be 22cm*15cm*6cm.
Thanks all, we look forward to seeing the designs!
Target Market(s)
Parents / adults
Industry/Entity Type
Baby
Look and feel

```html
<!DOCTYPE html>
<html lang="en">
<head>
<meta charset="utf-8">
<title>Quellora Cloth Diaper Sprayer – Packaging</title>
<link href="https://fonts.googleapis.com/css2?family=Comfortaa:wght@400&family=Raleway:wght@400;600;700&family=Open+Sans:ital,wght@0,400;0,600;1,400&display=swap" rel="stylesheet">
<style>
  :root{
    --bg:#9d9d9d;
    --aqua:#bfe7e6;
    --aqua-soft:#e4f6f5;
    --blue:#2b8fd6;
    --blue-deep:#1d6fc4;
    --blue-light:#49aee4;
    --brand:#2a7fd0;
    --green:#2fb89a;
    --lime:#d7e84a;
    --white:#ffffff;
    --grey-text:#8a8f94;
  }
  *{box-sizing:border-box;margin:0;padding:0}
  html,body{width:1200px;height:927px;overflow:hidden;background:var(--bg)}
  .canvas{position:relative;width:1200px;height:927px}
  .panel{position:absolute;top:53px;width:560px;height:820px;overflow:hidden;background:var(--white)}
  .panel--back{left:25px}
  .panel--front{left:615px}
  .panel__bg{position:absolute;inset:0;width:100%;height:100%}

  /* back */
  .contents-title{position:absolute;top:34px;width:100%;text-align:center;font:400 17px "Raleway",sans-serif;color:var(--blue-deep)}
  .contents{position:absolute;top:70px;left:20px;right:20px;display:flex;justify-content:space-between}
  .item{width:120px;text-align:center}
  .item__img{width:104px;height:104px;margin:0 auto;border-radius:50%;background:radial-gradient(circle,#f4f6f7 45%,#d2d8dc);border:5px solid var(--aqua-soft)}
  .item__label{margin-top:8px;font:400 10px/1.3 "Open Sans",sans-serif;color:var(--grey-text)}
  .instructions{position:absolute;top:302px;left:24px;right:24px;color:var(--white);font:400 11px/1.35 "Open Sans",sans-serif}
  .instructions h3{font:600 12px "Open Sans",sans-serif;color:var(--lime);border-bottom:1px solid var(--white);padding-bottom:3px;margin-bottom:6px}
  .instructions .important{margin-bottom:8px}
  .instructions ol{padding-left:18px}
  .instructions li{margin-bottom:5px}
  .note{text-align:center;font-style:italic;font-size:10px;margin-top:6px}
  .slogan{position:absolute;top:648px;width:100%;text-align:center;font:600 12.5px/1.3 "Open Sans",sans-serif;color:var(--lime)}
  .howto{position:absolute;top:698px;left:24px;width:240px;font:400 10px/1.35 "Open Sans",sans-serif;color:var(--white)}
  .howto h4{font:600 11px "Open Sans",sans-serif;color:var(--lime);margin-bottom:2px}
  .warning{position:absolute;top:698px;right:24px;width:250px;border:1px solid var(--white);padding:10px 12px;font:400 10px/1.35 "Open Sans",sans-serif;color:var(--white);text-align:center}

  /* front */
  .brand{position:absolute;top:112px;width:100%;display:flex;justify-content:center;align-items:center;gap:12px}
  .brand__name{font:700 66px "Raleway",sans-serif;color:var(--brand);letter-spacing:1px}
  .brand__dot{width:20px;height:20px;border-radius:50%;background:var(--brand)}
  .title{position:absolute;top:268px;width:100%;text-align:center;font:400 40px "Comfortaa",sans-serif;color:var(--blue-deep)}
  .tagline{position:absolute;top:330px;width:100%;text-align:center;font:400 17px "Raleway",sans-serif;color:var(--green);letter-spacing:.5px}
  .product{position:absolute;top:372px;left:30px;width:500px;height:300px}
  .product__part{position:absolute;width:118px;height:118px;border-radius:50%;background:radial-gradient(circle,#f3f6f7 45%,#cfd6da);border:5px solid var(--aqua-soft)}
  .product__hero{position:absolute;left:230px;top:0;width:250px;height:300px;border-radius:40px 40px 20px 20px;background:linear-gradient(90deg,#8d949b,#e6e9ec 45%,#9aa1a8 80%,#c9e8f3)}
  .features{position:absolute;top:708px;width:100%;text-align:center;list-style:none;font:400 14px/1.5 "Open Sans",sans-serif;color:var(--white)}
</style>
</head>
<body>
<main class="canvas">

  <section class="panel panel--back" aria-label="Back of box">
    <svg class="panel__bg" viewBox="0 0 560 820" preserveAspectRatio="none" aria-hidden="true">
      <defs>
        <linearGradient id="backBlue" x1="0" y1="0" x2="0" y2="1">
          <stop offset="0" stop-color="#4cb1e6"/>
          <stop offset="1" stop-color="#1d6fc4"/>
        </linearGradient>
      </defs>
      <rect width="560" height="820" fill="url(#backBlue)"/>
      <path d="M0 0H560V230Q300 300 0 250Z" fill="#ffffff"/>
      <path d="M0 250Q300 300 560 230" fill="none" stroke="#bfe7e6" stroke-width="6"/>
    </svg>

    <h2 class="contents-title">INSIDE CONTAINS:</h2>
    <div class="contents">
      <div class="item"><div class="item__img" role="img" aria-label="Chrome sprayer head"></div><p class="item__label">Brass Sprayer<br>Head</p></div>
      <div class="item"><div class="item__img" role="img" aria-label="Coiled stainless steel hose"></div><p class="item__label">1.5m Stainless<br>Steel Hose</p></div>
      <div class="item"><div class="item__img" role="img" aria-label="Three way T-adapter valve"></div><p class="item__label">3 Way T-adapter with<br>rubber washer<br>(Size: 7/8" • 7/8" • ½")</p></div>
      <div class="item"><div class="item__img" role="img" aria-label="Metal sprayer holder"></div><p class="item__label">Sprayer Holder</p></div>
    </div>

    <div class="instructions">
      <h3>INSTALLATION INSTRUCTIONS:</h3>
      <p class="important">IMPORTANT! Your toilet must have a flexible supply line to install a Quellora Cloth Diaper Sprayer (Flexible hose not included).</p>
      <ol>
        <li>Shut off water supply to the toilet by turning the water valve all the way to the right (should be a tap on the wall), flush the toilet and hold down the handle to drain the tank.</li>
        <li>Disconnect the flexible water supply line from under the toilet tank.</li>
        <li>Ensure the rubber washer is placed properly inside the top of the 3-way T-adapter before connecting it to the toilet tank. Afterwards, reconnect the flexible water supply line to the bottom end of the 3-way T-adapter (do not overtighten).</li>
        <li>Ensure that the rubber washers are placed properly on EACH end of the metal hose; attach one end of the hose to the open end of the 3-way T-adapter and the other end to the sprayer head.</li>
        <li>Lift the toilet water tank lid and hang the sprayer holder over the edge of the tank. Close the toilet tank lid.</li>
        <li>Turn the water supply line valve back on (the one that was turned off in step 1). Inspect for leaks upon completing installation and again after 10 minutes. Use plumbers tape on any leaking joints.</li>
      </ol>
      <p class="note">After following these steps, you are now ready to use your cloth diaper sprayer.<br>The whole installation should take no longer than 10 minutes and should require no tools.</p>
    </div>

    <p class="slogan">IT HAS NEVER BEEN EASIER TO INSTALL A CLOTH DIAPER SPRAYER<br>IN YOUR OWN BATHROOM.</p>

    <div class="howto">
      <h4>HOW TO USE:</h4>
      <p>Step 1: Open the T-adapter to allow water to flow.</p>
      <p>Step 2: Press the lever to release the water from the sprayer head.</p>
      <p>Step 3: Adjust to your desired water pressure by gently turning the handle of the T-adapter whilst holding down the lever on the sprayer.</p>
    </div>
    <p class="warning">WARNING! When the sprayer is not in use, please switch the T-adapter off. Failure to do so may weaken the hose or sprayer head. Quellora is not responsible for damages that may be caused by the failure to follow this warning.</p>
  </section>

  <section class="panel panel--front" aria-label="Front of box">
    <svg class="panel__bg" viewBox="0 0 560 820" preserveAspectRatio="none" aria-hidden="true">
      <defs>
        <linearGradient id="topAqua" x1="0" y1="0" x2="0" y2="1">
          <stop offset="0" stop-color="#bfe7e6"/>
          <stop offset="1" stop-color="#e9f8f7"/>
        </linearGradient>
        <linearGradient id="frontBlue" x1="0" y1="0" x2="0" y2="1">
          <stop offset="0" stop-color="#3aa3e0"/>
          <stop offset="1" stop-color="#1d6fc4"/>
        </linearGradient>
      </defs>
      <rect width="560" height="820" fill="#ffffff"/>
      <path d="M0 0H560V200Q300 270 0 220Z" fill="url(#topAqua)"/>
      <path d="M0 700Q300 640 560 660V820H0Z" fill="url(#frontBlue)"/>
      <path d="M0 700Q300 640 560 660" fill="none" stroke="#bfe7e6" stroke-width="5"/>
    </svg>

    <div class="brand"><span class="brand__name">Quellora</span><span class="brand__dot"></span></div>
    <h1 class="title">Cloth Diaper Sprayer</h1>
    <p class="tagline">RINSE FRESH LIVE GREEN</p>

    <div class="product">
      <div class="product__part" style="left:0;top:10px" role="img" aria-label="T-adapter valve"></div>
      <div class="product__part" style="left:95px;top:80px" role="img" aria-label="Sprayer holder"></div>
      <div class="product__part" style="left:5px;top:150px" role="img" aria-label="Coiled metal hose"></div>
      <div class="product__hero" role="img" aria-label="Chrome hand sprayer with water splash"></div>
    </div>

    <ul class="features">
      <li>Includes Brass Sprayer head, metal hose, T-adapter and holder</li>
      <li>Fits standard North American style toilets</li>
      <li>EASY installation – NO plumber or tools needed</li>
      <li>The easy way to clean cloth diapers</li>
      <li>Perfect for personal and feminine hygiene</li>
    </ul>
  </section>

</main>
</body>
</html>
```